Fantastische (!) Zusammenarbeit!! Reibungslose und schnelle Kommunikation. Änderungswünsche werden sofort entgegengenommen und umgesetzt. Soweit etwas nicht passt, wird so lange weiterverändert, bis es passt. Einfach super. Nachfragen werden binnen kürzester Zeit beantwortet - auch für allgemeine Fragen ein super Ansprechpartner. Danke hierfür ! Auch nach Ablauf des Projektes ist der Designer jederzeit ansprechbar und gibt gerne Hilfestellung. So stellt man sich Service vor! Ich kann KP47 wärmstens empfehlen. Jederzeit wieder. Die Rundum-Leistung ist klasse und das Endprodukt ohnehin super ! Nochmal herzlichen Dank!
Zielgruppe
Derzeit befinde ich mich in der Gründungsphase einer Softwarefirma namens 'Braukon-Solutions'. Nach der Namensfindung wird nun ein Corporate-Design benötig, bestehend aus einem ansprechendem Logo mit Wiedererkennungswert, einem Briefpapier für Korrespondenz und Rechnungen, sowie einer Visitenkarte inkl. QR-Code.
Tätigkeit:
Software- und Datenbankentwicklung für Firmenkunden
Zielgruppen:
sämtliche Firmen, die individuelle Softwarelösungen suchen
Was sind wir - folgende Merkmale sollen mit dem Logo visualisiert werden.
engagiert
- weil die Interessen der Kunden immer im Fokus der Zusammenarbeit stehen.
kompetent
- weil wir über hohes fachliches Know-How verfügen.
flexibel
- weil die Braukon-Solutions durch ein kleines, professionelles Team auf veränderte
Situationen sofort reagieren kann.
qualitätsbewusst
- weil die Braukon-Solutions keine Kompromisse macht wenn es um die Beratung und
Betreuung ihrer Kunden geht.
verlässlich
- weil langfristige und vertrauensvolle Beziehungen zu Geschäftspartnern zu den Grundprinzipiens unseres Handelns gehört.
unkonventionell und individuell
- weil die Braukon-Solutions immer bereit ist, im Interesse ihrer Kunden zu handeln
und unkonventionelle nicht zwingend branchentypische Lösungen zu schaffen.
Aufgabenstellung
Das Design soll klar strukturiert, modern und professionell sein. Kommuniziert werden sollen Vertrauen, Kompetenz, partnerschaftliche Zusammenarbeit, Individualität und Verlässlichkeit.
Bestehend aus einem ansprechendem Logo mit Wiedererkennungswert, einem Briefpapier für Korrespondenz und Rechnungen, sowie einer Visitenkarte inkl. QR-Code.

```html
<!DOCTYPE html>
<html lang="de">
<head>
<meta charset="utf-8">
<title>Braukon Solutions – Geschäftsausstattung</title>
<link rel="stylesheet" href="https://fonts.googleapis.com/css2?family=Open+Sans:wght@400;600;700&family=Quicksand:wght@500;600;700&display=swap">
<style>
  :root {
    --bg: #2c2d31;
    --paper: #ffffff;
    --ink: #2f323a;
    --ink-soft: #3c3f4a;
    --green: #b2c545;
    --grey-line: #cfd0d3;
    --sig: #e6e6e8;
  }
  * { box-sizing: border-box; margin: 0; padding: 0; }
  html, body { width: 1200px; height: 856px; overflow: hidden; background: var(--bg); }
  .canvas { position: relative; width: 1200px; height: 856px; }

  .brand-name {
    font-family: "Quicksand", sans-serif;
    font-weight: 600;
    color: var(--ink-soft);
    display: flex; align-items: center; gap: 5px;
    white-space: nowrap;
  }
  .brand-name .mark { display: inline-block; background: var(--green); }

  /* Letterhead */
  .letterhead {
    position: absolute; left: 175px; top: 135px; width: 416px; height: 588px;
    background: var(--paper);
    font-family: "Open Sans", sans-serif; color: var(--ink);
  }
  .letterhead .brand-name { position: absolute; right: 44px; top: 46px; font-size: 14px; }
  .letterhead .brand-name .mark { width: 12px; height: 12px; }
  .sender-line {
    position: absolute; left: 45px; top: 88px;
    font-size: 4.2px; font-weight: 700; border-bottom: 0.6px solid var(--ink); padding-bottom: 1px;
  }
  .recipient { position: absolute; left: 45px; top: 107px; font-size: 6px; line-height: 8px; }
  .recipient .city { margin-top: 8px; }
  .subject { position: absolute; left: 45px; top: 200px; font-size: 6px; font-weight: 700; }
  .body { position: absolute; left: 45px; top: 222px; width: 226px; font-size: 5.6px; line-height: 7.6px; }
  .body p + p { margin-top: 5px; }
  .closing { position: absolute; left: 45px; top: 420px; font-size: 5.6px; }
  .signature { position: absolute; left: 45px; top: 434px; width: 90px; height: 18px; background: var(--sig); border-radius: 2px; }
  .signer { position: absolute; left: 45px; top: 459px; font-size: 5.6px; }
  .footer { position: absolute; left: 43px; top: 544px; display: flex; height: 44px; }
  .footer .col {
    border-left: 0.8px solid var(--green); padding: 3px 0 0 5px;
    font-family: "Quicksand", sans-serif; font-weight: 600; font-size: 4.2px; line-height: 6.8px; letter-spacing: 0.2px;
  }
  .footer .col-address { width: 96px; }
  .footer .col-contact { width: 105px; }
  .footer .col-bank { width: 90px; }

  /* Business cards */
  .card { position: absolute; left: 770px; width: 253px; height: 163px; }
  .card-front { top: 221px; background: var(--paper); color: var(--ink-soft); font-family: "Quicksand", sans-serif; }
  .card-front .brand-name { position: absolute; left: 18px; top: 22px; font-size: 16px; }
  .card-front .brand-name .mark { width: 14px; height: 14px; }
  .person { position: absolute; left: 18px; top: 64px; }
  .person .name { font-size: 10px; font-weight: 700; letter-spacing: 0.3px; }
  .person .role { font-size: 6.6px; color: var(--green); letter-spacing: 0.4px; }
  .card-address { position: absolute; left: 18px; top: 92px; font-size: 7px; line-height: 9.6px; font-weight: 600; letter-spacing: 0.3px; }
  .card-contact { position: absolute; left: 18px; top: 115px; font-size: 7px; line-height: 9px; font-weight: 600; letter-spacing: 0.3px; }
  .card-contact .label { color: var(--green); }
  .card-web { position: absolute; left: 18px; top: 140px; font-size: 6.6px; color: var(--green); font-weight: 600; letter-spacing: 0.8px; }

  .card-back { top: 472px; background: var(--green); display: flex; align-items: center; justify-content: center; }
  .card-back .brand-name { color: #ffffff; font-size: 18px; }
</style>
</head>
<body>
<main class="canvas">

  <section class="letterhead">
    <div class="brand-name"><span class="mark"></span>Braukon Solutions</div>
    <div class="sender-line">Vorname Nachname, Am Kai 12, 12345 Beispielstadt</div>
    <div class="recipient">
      <div>Lena Hofmann</div>
      <div>Lindenweg 456</div>
      <div class="city">12345 Berlin</div>
    </div>
    <div class="subject">Quidero molore, atatur sae. Nequat,</div>
    <div class="body">
      <p>Ur sit, imus, ipicatem voluptate eum re dolluptios sequosam, eum reritati am volor sapedissi quo blaboribust, sequass itasped igendi cus exerfer feruptas iusanda ndaest, qui omnis nus aut fugitinis quatur ad ullaut mostem quasperiae corem et aciatem illatin ciduntores quidis utemquam autemperae soluptiae lab illacescia solorum et fugiam ratatatus exerro blaciis samusam etur? Uga. Neque nam simi, nest, ommod essedios magnatia nossi aute nonsequam fugiaspis moluptas sed el int etur saepe nonsecatem excea noneceperrum ulligendit faccullores et lantur si ium at. Ota cuptae non ea de opta voles rem rae dolore ilia vellab isi blanis idit veribus auda alit labore desenis imenis que in con rehent, explat ped que volorum, autent, si tetur?</p>
      <p>Ihil ium restior ecepero reptistius es aborepe diatiunt dignis diciae voluptu ribearit, que nat aute et as maximus, qui blab iur aut volest, nonsequae odios doluptatiae velignimin perescia vent. Pa voluptas expero corectur molest eaquid enda vidus verciis quodi te dit aliquid unturem poreper feratur? Quis aut rehenihilit et quam, eris et perorru mquamusa quo et untia volupie nisimoluptae esseribus cora doluptati doluptatur atisciumqui re pa quat aut lam solescia intiis et millabor sit odis et quos re sam, vendicientur abo. Equi totatus rest, nosam quodi omni doloriosam des ea nimpelique volo elendae dellign ihilitis solupta temporp orupta iuntia ipiste natibusapis volesedis reriori taerrup tatiberes nobitiur, sequi omnihillab id maximagnat omnimus dolo quunt, int aut earum lacit peliquunt iduciet, id que autemolum deruptati te non re.</p>
    </div>
    <div class="closing">Sincerely</div>
    <div class="signature" role="img" aria-label="Handschriftliche Unterschrift"></div>
    <div class="signer">Jonas Albrecht</div>
    <div class="footer">
      <div class="col col-address">Vorname Nachname<br>Am Kai 12<br>12345 Beispielstadt</div>
      <div class="col col-contact">tel.: 030 - 555 018 2<br>mail: info@braukon-beispiel.de<br>www.braukon-beispiel.de</div>
      <div class="col col-bank">Hafenbank GmbH<br>IBAN: DE00123400567<br>BIC: HAFBDE00XX</div>
    </div>
  </section>

  <section class="card card-front">
    <div class="brand-name"><span class="mark"></span>Braukon Solutions</div>
    <div class="person">
      <div class="name">Name Vorname</div>
      <div class="role">Geschäftsführer</div>
    </div>
    <div class="card-address">Am Kai 12<br>12345 Beispielstadt</div>
    <div class="card-contact">
      <div><span class="label">mail:</span> info@braukon-beispiel.de</div>
      <div><span class="label">tel.:</span> +49 (0) 30 - 555 018-2</div>
    </div>
    <div class="card-web">www.braukon-beispiel.de</div>
  </section>

  <section class="card card-back">
    <div class="brand-name">Braukon</div>
  </section>

</main>
</body>
</html>
```